Original business card of a small accounting firm

My firm specializes in accounting and taxes for small businesses. I'm looking for an original and creative business card as a marketing tool to give to prospective clients; however since we are a professional firm the card must also appear professional. I'm uploading a few examples of what I believe may fit my needs. Please feel free to use them as a jumping off point. Lastly, I'm uploading the company logo which I'd like to be the focal point on the back of the card and somewhat incorporated on the front on a smaller scale. I hope my description was helpful.
Target Market(s)
Tax clients and small businesses
Industry/Entity Type
Accounting
Contact Information for Business Card
Leonard Whitcombe
Certified Public Accountant │President
Kestrel Advisors
T│ (555) 418-2763
Email│LWhitcombe@KestrelAdvisors.example

```html
<!DOCTYPE html>
<html lang="en">
<head>
<meta charset="utf-8">
<title>Kestrel Advisors – Business Card</title>
<link rel="stylesheet" href="https://fonts.googleapis.com/css2?family=Arimo:wght@400;700&family=Cinzel:wght@400&family=Questrial&display=swap">
<style>
  :root {
    --backdrop: #e6e6e8;
    --card-dark: #1f1d1f;
    --card-light: #ffffff;
    --wordmark-grey: #b7babf;
    --tagline-grey: #9fa2a7;
    --brand-blue: #3e72cf;
    --name-blue: #2c3a9c;
    --body-text: #2a2a2a;
    --mark-tint-a: #d9dbf1;
    --mark-tint-b: #f4f5fb;
  }
  * { box-sizing: border-box; margin: 0; padding: 0; }
  html, body {
    width: 1200px;
    height: 1000px;
    overflow: hidden;
    background: var(--backdrop);
  }
  .sheet {
    position: relative;
    width: 1200px;
    height: 1000px;
  }
  .card {
    position: absolute;
    left: 260px;
    width: 680px;
    height: 388px;
    border-radius: 4px;
    box-shadow: 0 6px 18px rgba(0, 0, 0, 0.18);
    overflow: hidden;
  }

  /* Back of card */
  .card--back {
    top: 52px;
    background: var(--card-dark);
    display: flex;
    flex-direction: column;
    align-items: center;
    justify-content: center;
  }
  .brand-lockup {
    display: flex;
    align-items: center;
    gap: 18px;
  }
  .brand-square {
    width: 34px;
    height: 34px;
    background: var(--brand-blue);
  }
  .brand-name {
    font-family: "Questrial", sans-serif;
    font-size: 46px;
    color: var(--wordmark-grey);
    letter-spacing: 0.5px;
  }
  .brand-tagline {
    margin-top: 12px;
    font-family: "Cinzel", serif;
    font-size: 15px;
    letter-spacing: 3.2px;
    color: var(--tagline-grey);
    text-transform: uppercase;
  }

  /* Front of card */
  .card--front {
    top: 530px;
    background: var(--card-light);
  }
  .brand-watermark {
    position: absolute;
    left: 40px;
    top: 64px;
    width: 240px;
    height: 240px;
    background: linear-gradient(135deg, var(--mark-tint-a), var(--mark-tint-b));
  }
  .contact {
    position: absolute;
    left: 300px;
    top: 110px;
    font-family: "Arimo", sans-serif;
    color: var(--body-text);
  }
  .contact__name {
    font-size: 30px;
    font-weight: 700;
    color: var(--name-blue);
    text-transform: uppercase;
    letter-spacing: 0.5px;
  }
  .contact__role {
    margin-top: 6px;
    font-size: 19px;
    line-height: 1.25;
  }
  .contact__line {
    display: flex;
    align-items: center;
    gap: 10px;
    margin-top: 12px;
    font-size: 19px;
  }
  .contact__line:first-of-type { margin-top: 18px; }
  .contact__icon {
    width: 20px;
    height: 20px;
    flex: none;
  }
</style>
</head>
<body>
  <main class="sheet">
    <section class="card card--back" aria-label="Card back">
      <div class="brand-lockup">
        <span class="brand-square" aria-hidden="true"></span>
        <span class="brand-name">Kestrel Advisors</span>
      </div>
      <p class="brand-tagline">Small Business Accounting and Taxes</p>
    </section>

    <section class="card card--front" aria-label="Card front">
      <div class="brand-watermark" role="img" aria-label="Faint Kestrel Advisors brand mark area"></div>
      <div class="contact">
        <h1 class="contact__name">Leonard Whitcombe</h1>
        <p class="contact__role">Certified Public Accountant<br>President Kestrel Advisors</p>
        <p class="contact__line">
          <svg class="contact__icon" viewBox="0 0 24 24" aria-hidden="true">
            <path d="M6.6 2.5c.6-.3 1.2 0 1.5.5l2 3.6c.3.5.2 1.1-.2 1.5L8.3 9.6c.9 2.3 3.7 5.1 6.1 6.1l1.5-1.6c.4-.4 1-.5 1.5-.2l3.6 2c.5.3.8.9.5 1.5l-1 2.3c-.3.7-1 1.1-1.8 1C10.6 20 4 13.4 3.3 5.3c-.1-.8.3-1.5 1-1.8z" fill="#111"/>
          </svg>
          <span>(555) 418-2763</span>
        </p>
        <p class="contact__line">
          <svg class="contact__icon" viewBox="0 0 24 24" aria-hidden="true">
            <rect x="2" y="5" width="20" height="14" fill="#111"/>
            <path d="M2.5 5.5 12 13l9.5-7.5" fill="none" stroke="#fff" stroke-width="1.5"/>
          </svg>
          <span>LWhitcombe@KestrelAdvisors.example</span>
        </p>
      </div>
    </section>
  </main>
</body>
</html>
```